VELMOR Website Design

We need a website designed for our company VELMOR. We are a luxury lifestyle club that will provide benefits and services for our members. The site should be clean & sleek, preferably using black and white (or darker colors). (example sites: brastelle.com, fovix.com)

Here is a link of a sample page I did using wix. (https://dunmerel7.pagebuildr.com/mysite) This can be used to get a general idea.

Target Market(s)

Upper Middle Class in the United States

Number of Pages Required

5+ page

Font styles to use
Sans Serif
Other font styles liked:
• Arial (or other similar fonts)

Requirements
Must have
• A clean design that is eye-catching and speaks to our company.
Nice to have
• Ideas for copy.

```html
<!DOCTYPE html>
<html lang="en">
<head>
<meta charset="utf-8">
<title>VELMOR — The ultimate full service lifestyle club</title>
<link rel="stylesheet" href="https://fonts.googleapis.com/css2?family=Lato:wght@300;400;700&display=swap">
<style>
  :root{
    --ink:#000000;
    --paper:#ffffff;
    --navy:#0b1733;
    --night:#1a1433;
    --plum:#2b1d45;
    --band:rgba(16,20,40,0.72);
    --mist:rgba(255,255,255,0.38);
    --muted:#bfc3cc;
  }
  *{margin:0;padding:0;box-sizing:border-box}
  html,body{width:1200px;height:4030px;overflow:hidden;background:var(--ink)}
  body{position:relative;font-family:"Lato",Arial,sans-serif;color:var(--paper);font-weight:300}
  .layer{position:absolute;left:0;width:1200px}

  /* backgrounds */
  .services-bg{top:1100px;height:1900px;z-index:1;
    background:radial-gradient(circle at 20% 30%,#3a2a5a 0,transparent 40%),
               radial-gradient(circle at 80% 70%,#3b2450 0,transparent 45%),
               linear-gradient(180deg,var(--night),var(--plum) 60%,#24193d)}
  .hero-photo{top:0;height:900px;z-index:2;
    clip-path:polygon(0 0,1200px 0,1200px 645px,0 885px);
    background:linear-gradient(120deg,#6b5a4c 0%,#b89a7e 35%,#8a6d5a 60%,#3d2f2a 100%)}
  .about-photo{top:660px;height:700px;z-index:3;
    clip-path:polygon(0 215px,595px 10px,595px 640px,0 680px);
    background:linear-gradient(110deg,#7d6a55 0%,#c9b193 40%,#9a8a6a 70%,#6e7b5a 100%)}
  .about-panel{top:640px;height:700px;z-index:3;
    clip-path:polygon(595px 145px,1200px 5px,1200px 540px,595px 680px);
    background:linear-gradient(160deg,#0f1d3e,var(--navy) 70%,#0a1228)}
  .join-photo{top:2860px;height:815px;z-index:4;
    clip-path:polygon(0 10px,1200px 275px,1200px 815px,0 815px);
    background:linear-gradient(180deg,#6fa7d6 0%,#a9d0ea 30%,#3fa9b8 48%,#d9d3c3 62%,#ece7dc 100%)}
  .join-panel{top:2860px;height:815px;z-index:5;
    clip-path:polygon(620px 815px,1200px 290px,1200px 815px);
    background:var(--mist)}
  .footer{top:3675px;height:355px;z-index:6;background:var(--ink);text-align:center}

  /* nav */
  .nav{top:0;height:70px;z-index:10}
  .brand{position:absolute;left:50px;top:16px;font-size:34px;font-weight:400;letter-spacing:2px}
  .menu{position:absolute;right:20px;top:18px;display:flex;align-items:center;gap:20px;font-size:17px;font-weight:400;letter-spacing:.5px}
  .menu .current{border-bottom:1px solid var(--paper);padding-bottom:2px}
  .btn{display:inline-block;background:var(--paper);color:var(--ink);font-weight:700;letter-spacing:1px;text-align:center}
  .menu .btn{padding:6px 22px;font-size:17px}

  /* hero */
  .hero{top:0;height:670px;z-index:10;text-align:center}
  .hero h1{position:absolute;top:180px;width:100%;font-size:68px;font-weight:300;letter-spacing:4px}
  .hero p{position:absolute;top:318px;width:100%;font-size:28px}
  .hero .btn{position:absolute;top:402px;left:540px;width:120px;height:46px;line-height:46px;font-size:24px}

  /* section headings */
  .heading{position:absolute;right:60px;text-align:right;font-size:46px;font-weight:300;letter-spacing:1px}
  .heading::after{content:"";display:block;height:2px;background:var(--paper);margin-top:12px;margin-left:auto}

  .about{top:640px;height:700px;z-index:10}
  .about .heading{top:55px}
  .about .heading::after{width:170px}
  .about p{position:absolute;left:695px;top:180px;width:450px;font-size:17px;line-height:25px;font-weight:400}
  .about .btn{position:absolute;right:60px;top:305px;padding:9px 16px;font-size:20px}

  .services{top:1350px;height:1400px;z-index:10}
  .services .heading{top:20px}
  .services .heading::after{width:525px}
  .circle{position:absolute;width:340px;height:340px;border-radius:50%;overflow:hidden}
  .circle .label{position:absolute;left:0;bottom:0;width:100%;height:112px;background:var(--band);
    text-align:center;padding-top:26px;font-size:27px;font-weight:700}
  .c1{left:54px}.c2{left:430px}.c3{left:802px}
  .r1{top:240px}.r2{top:645px}.r3{top:1025px}

  .join{top:3150px;height:520px;z-index:10}
  .join .heading{top:115px}
  .join .heading::after{width:170px}
  .join p{position:absolute;right:60px;top:240px;width:430px;text-align:right;font-size:16px;line-height:23px;font-weight:400}
  .join .btn{position:absolute;right:60px;top:330px;padding:8px 16px;font-size:18px}

  .social{position:absolute;top:95px;width:100%;display:flex;justify-content:center;gap:44px;font-size:24px;font-weight:700}
  .copyright{position:absolute;top:268px;width:100%;font-size:16px;letter-spacing:1px;font-weight:400}
  .legal{position:absolute;top:302px;width:100%;font-size:13px;color:var(--muted);font-weight:400}
</style>
</head>
<body>
  <div class="layer services-bg" role="img" aria-label="Deep purple night background with soft glowing bokeh lights"></div>
  <div class="layer hero-photo" role="img" aria-label="Photo of guests raising wine glasses at an elegant party"></div>
  <div class="layer about-photo" role="img" aria-label="Photo of well-dressed friends toasting with champagne outdoors"></div>
  <div class="layer about-panel"></div>
  <div class="layer join-photo" role="img" aria-label="Photo of a woman relaxing on a lounge chair with a laptop on a tropical beach"></div>
  <div class="layer join-panel"></div>

  <header class="layer nav">
    <div class="brand">VELMOR</div>
    <nav class="menu">
      <span class="current">HOME</span>
      <span>ABOUT</span>
      <span>SERVICES &amp; BENEFITS</span>
      <span class="btn">JOIN</span>
    </nav>
  </header>

  <section class="layer hero">
    <h1>VELMOR</h1>
    <p>The ultimate full service lifestyle club</p>
    <span class="btn">JOIN</span>
  </section>

  <section class="layer about">
    <h2 class="heading">ABOUT</h2>
    <p>VELMOR is a members only lifestyle club founded in order to bring the best services, experiences, and opportunities to our diverse community of members. Our members consist of creatives, athletes, artists, and other professionals.</p>
    <span class="btn">LEARN MORE</span>
  </section>

  <section class="layer services">
    <h2 class="heading">SERVICES AND BENEFITS</h2>
    <div class="circle c1 r1" role="img" aria-label="Photo of a calculator and paperwork" style="background:linear-gradient(150deg,#e8e8e8,#9a9a9a 60%,#3a3a3a)"><div class="label">Accounting</div></div>
    <div class="circle c2 r1" role="img" aria-label="Photo of banknotes and a growing plant" style="background:linear-gradient(150deg,#9fb48a,#5c6b4a 55%,#2e2a22)"><div class="label">Investment</div></div>
    <div class="circle c3 r1" role="img" aria-label="Photo of a personal document folder" style="background:linear-gradient(150deg,#e9dcc6,#b33a2a 55%,#5a1a14)"><div class="label">Lawyer</div></div>
    <div class="circle c1 r2" role="img" aria-label="Photo of a large house with trees" style="background:linear-gradient(170deg,#a8c4d8,#7c8f5a 45%,#8a5a3a 75%,#3d4a2a)"><div class="label">Real Estate</div></div>
    <div class="circle c2 r2" role="img" aria-label="Photo of a hotel service desk bell" style="background:linear-gradient(150deg,#f1ece2,#d6cbb5 60%,#8f8470)"><div class="label">24/7 Coincerage</div></div>
    <div class="circle c3 r2" role="img" aria-label="Photo of a private jet on the runway" style="background:linear-gradient(180deg,#c9d4de,#8d9aa8 55%,#4c5560)"><div class="label">Private Jet Travel</div></div>
    <div class="circle c1 r3" role="img" aria-label="Photo of a concert crowd at sunset" style="background:linear-gradient(160deg,#f0a350,#c8642a 50%,#3a2030)"><div class="label">Event Access</div></div>
    <div class="circle c2 r3" role="img" aria-label="Photo of a guest at an intimate private gathering" style="background:linear-gradient(160deg,#6c8fb0,#c49a86 50%,#3a3040)"><div class="label">Private Events</div></div>
    <div class="circle c3 r3" role="img" aria-label="Photo of a climber on a rocky cliff" style="background:linear-gradient(160deg,#b98a5c,#6e4a30 55%,#2e2018)"><div class="label">Experiences</div></div>
  </section>

  <section class="layer join">
    <h2 class="heading">JOIN US</h2>
    <p>Join us for exclusive access and enjoy the benefits that only come with being a member.</p>
    <span class="btn">JOIN</span>
  </section>

  <footer class="layer footer">
    <div class="social"><span>Flitter</span><span>Facade</span><span>Snapgram</span><span>Glowva</span></div>
    <div class="copyright">COPYRIGHT © 2018, ALL RIGHTS RESERVED.</div>
    <div class="legal">Terms and Conditions | Service Policies | Back to Top</div>
  </footer>
</body>
</html>
```